Harbor Ridge Seed Collective business cards

Create a single-sided business card for the Harbor Ridge Seed Collective based on the attached logo.
The additional data fields include Name, Title, Email, Phone, and website.
Please use the following as sample data:
Name: Dana Vellor
Title: Co-Founder / Investor
Email: danavellor@mailbrook.example
Phone: 805-555-0147
Website: www.hrseedcollective.example

Target Market(s)

Start ups, entrepreneurs, venture capitalists

Industry/Entity Type

Investment

Contact Information for Business Card

Professional business card. Technology company.

Font styles to use
Serif
Sans Serif

Requirements
Must have
• Include the HRSC logo (attached)
• Name
• Title
• Email
• Phone
• Website
Should not have
• Cute, cartoony

```html
<!DOCTYPE html>
<html lang="en">
<head>
<meta charset="utf-8">
<title>Harbor Ridge Seed Collective — Business Card</title>
<link rel="stylesheet" href="https://fonts.googleapis.com/css2?family=Open+Sans:wght@400;600;700&display=swap">
<style>
  :root {
    --backdrop: #ece9e4;
    --card: #ffffff;
    --green: #1e9e58;
    --green-deep: #15864a;
    --green-light: #3fb877;
    --ink: #2f3133;
    --muted: #5d6064;
    --shadow: rgba(0,0,0,.18);
  }
  * { box-sizing: border-box; margin: 0; padding: 0; }
  html, body { width: 1200px; height: 950px; overflow: hidden; }
  body {
    background: var(--backdrop);
    font-family: "Open Sans", Arial, sans-serif;
    position: relative;
  }
  .card {
    position: absolute;
    width: 620px;
    height: 354px;
    background: var(--card);
    border-radius: 22px;
    box-shadow: 0 10px 28px var(--shadow);
    overflow: hidden;
  }
  /* Contact side */
  .card--contact { left: 90px; top: 100px; }
  .card--contact .accent {
    position: absolute; inset: 0; width: 100%; height: 100%;
  }
  .holder { position: absolute; left: 44px; top: 42px; }
  .holder__name {
    color: var(--green); font-weight: 700; font-size: 22px;
    letter-spacing: .5px; text-transform: uppercase;
  }
  .holder__title { color: var(--muted); font-size: 15px; margin-top: 4px; }
  .contacts {
    position: absolute; right: 40px; top: 44px;
    list-style: none; text-align: right;
  }
  .contacts li {
    display: flex; justify-content: flex-end; align-items: center; gap: 10px;
    color: var(--muted); font-size: 14px; line-height: 26px;
  }
  .contacts svg { width: 16px; height: 16px; flex: none; }
  .card--contact .brand {
    position: absolute; right: 44px; bottom: 48px;
    color: #ffffff; font-weight: 600; font-size: 24px; text-align: right;
    line-height: 1.2; width: 260px;
  }
  /* Logo side */
  .card--logo { left: 490px; top: 500px; }
  .logo-lockup {
    position: absolute; left: 70px; top: 92px; width: 480px;
  }
  .logo-lockup__mark {
    width: 56px; height: 56px; background: var(--green);
  }
  .logo-lockup__rule {
    height: 2px; background: var(--green); width: 430px; margin: 24px 0 18px;
  }
  .logo-lockup__name {
    color: var(--green); font-weight: 600; font-size: 34px; line-height: 1.15;
  }
</style>
</head>
<body>

<section class="card card--contact" aria-label="Business card, contact side">
  <svg class="accent" viewBox="0 0 620 354" preserveAspectRatio="none" role="img" aria-label="Green corner panel with soft translucent dot texture">
    <defs>
      <linearGradient id="panelFill" x1="0" y1="0" x2="1" y2="1">
        <stop offset="0" stop-color="var(--green-light)"/>
        <stop offset="1" stop-color="var(--green-deep)"/>
      </linearGradient>
    </defs>
    <polygon points="170,354 400,150 620,240 620,354" fill="url(#panelFill)"/>
  </svg>

  <div class="holder">
    <p class="holder__name">Dana Vellor</p>
    <p class="holder__title">Co-Founder / Investor</p>
  </div>

  <ul class="contacts">
    <li>805-555-0147
      <svg viewBox="0 0 16 16" aria-hidden="true"><path d="M4 1.5l2.2 3-1.3 1.6c.8 1.8 2.2 3.2 4 4l1.6-1.3 3 2.2-1.2 2.5C7 13.3 2.7 9 2.5 3.7z" fill="var(--green)"/></svg>
    </li>
    <li>danavellor@mailbrook.example
      <svg viewBox="0 0 16 16" aria-hidden="true"><rect x="1" y="3" width="14" height="10" rx="1.5" fill="var(--green)"/><path d="M1.5 4l6.5 5 6.5-5" stroke="#fff" stroke-width="1.3" fill="none"/></svg>
    </li>
    <li>www.hrseedcollective.example
      <svg viewBox="0 0 16 16" aria-hidden="true"><circle cx="8" cy="8" r="7" fill="var(--green)"/><path d="M1 8h14M8 1c-3 3.5-3 10.5 0 14M8 1c3 3.5 3 10.5 0 14" stroke="#fff" stroke-width="1" fill="none"/></svg>
    </li>
  </ul>

  <p class="brand">Harbor Ridge Seed Collective</p>
</section>

<section class="card card--logo" aria-label="Business card, logo side">
  <div class="logo-lockup">
    <div class="logo-lockup__mark"></div>
    <div class="logo-lockup__rule"></div>
    <p class="logo-lockup__name">Harbor Ridge<br>Seed Collective</p>
  </div>
</section>

</body>
</html>
```